Book Cover Design - Uncovering Weight Loss Secrets

I need a book cover design for a book called 'Folding The Map'. It is a book that goes through all of the secrets to weight loss, without any crazy shakes or workouts or pills or potions. The book is really focused on helping people understand that Weight loss is simple and has more to do with our mindset as well as the food we were eating. It is about taking personal responsibility not looking for the next fancy revolutionary product that is going to help them magically melt the fat away. The book is pragmatic in nature and breaks down in simple terms how we can lose weight and keep it off for the rest of our lives. It shows the user that it is simple to lose weight, but it takes effort. They should stop looking for a quick fix when it comes to weight loss but instead eat healthy for the rest of their lives.
The book is intended to be hard-hitting no holds barred approach. The book has the same title as my business name. I will attach the current logo that we use in the business. This doesn't need to be on the front of the book maybe at the back down the bottom somewhere.
I am looking to have both an e-book cover and a standard printed book cover.
I don't have any colours in mind, my logo can be adapted to be different colours or just white.
The message that I am wanting people to feel when they see my book, is that all these Weightloss fads are a joke, that I know the secrets that will get them to their weight loss goal even if they fail at everything else before.
On the cover it should say the following.
FOLDING THE MAP
Uncovering the Weight Loss Secrets
The big companies have been trying to keep hidden for years!
COLIN MAYHEW
People who have failed many times trying to lose weight & need help
Weight Loss

```html
<!DOCTYPE html>
<html lang="en">
<head>
<meta charset="utf-8">
<title>Folding The Map — Book Cover</title>
<link rel="stylesheet" href="https://fonts.googleapis.com/css2?family=Montserrat:wght@800;900&family=Roboto:wght@500&family=Oswald:wght@500;600&display=swap">
<style>
  :root {
    --page-bg: #e4e4e4;
    --cover-brown: #3b2013;
    --cover-brown-light: #46251a;
    --cover-edge: #2c170e;
    --figure-shade: #26150d;
    --ink-light: #e6e6e6;
    --title-shadow: #1c0f08;
  }
  * { margin: 0; padding: 0; box-sizing: border-box; }
  html, body {
    width: 1200px;
    height: 1067px;
    overflow: hidden;
    background: var(--page-bg);
  }
  .canvas {
    position: relative;
    width: 1200px;
    height: 1067px;
  }
  .book-cover {
    position: absolute;
    left: 277px;
    top: 53px;
    width: 646px;
    height: 960px;
    overflow: hidden;
    background: radial-gradient(ellipse at 50% 45%, var(--cover-brown-light) 0%, var(--cover-brown) 70%);
    box-shadow: 0 18px 40px rgba(0,0,0,0.25);
  }
  .edge-band {
    position: absolute;
    top: 0;
    bottom: 0;
    width: 40px;
    background: var(--cover-edge);
    opacity: 0.55;
  }
  .edge-band--left { left: 0; }
  .edge-band--right { right: 0; }
  .figure-art {
    position: absolute;
    left: 50px;
    top: 340px;
    width: 546px;
    height: 620px;
    background: linear-gradient(90deg,
      transparent 0%, var(--figure-shade) 12%, var(--figure-shade) 28%, transparent 40%,
      transparent 60%, var(--figure-shade) 72%, var(--figure-shade) 88%, transparent 100%);
    opacity: 0.55;
  }
  .title {
    position: absolute;
    top: 120px;
    left: 0;
    width: 100%;
    text-align: center;
    white-space: nowrap;
    font-family: "Montserrat", sans-serif;
    font-weight: 900;
    font-size: 92px;
    line-height: 0.98;
    letter-spacing: -1px;
    color: var(--ink-light);
    text-shadow: 6px 6px 0 var(--title-shadow);
  }
  .subtitle {
    position: absolute;
    top: 362px;
    left: 0;
    width: 100%;
    text-align: center;
    white-space: nowrap;
    font-family: "Roboto", sans-serif;
    font-weight: 500;
    font-size: 26px;
    line-height: 44px;
    color: var(--ink-light);
    text-shadow: 2px 2px 3px var(--title-shadow);
  }
  .secrets-band {
    position: absolute;
    left: 68px;
    width: 558px;
    top: 565px;
    height: 92px;
  }
  .secrets-band__rule {
    position: absolute;
    left: 0;
    right: 0;
    height: 10px;
    background: var(--ink-light);
  }
  .secrets-band__rule--top { top: 0; }
  .secrets-band__rule--bottom { bottom: 0; }
  .secrets-band__label {
    position: absolute;
    top: 10px;
    left: 0;
    right: 0;
    height: 72px;
    text-align: center;
    white-space: nowrap;
    font-family: "Oswald", sans-serif;
    font-weight: 600;
    font-size: 46px;
    line-height: 72px;
    letter-spacing: 3px;
    color: var(--ink-light);
  }
  .author {
    position: absolute;
    top: 790px;
    left: 0;
    width: 100%;
    text-align: center;
    white-space: nowrap;
    font-family: "Oswald", sans-serif;
    font-weight: 500;
    font-size: 38px;
    letter-spacing: 4px;
    color: var(--ink-light);
  }
</style>
</head>
<body>
<div class="canvas">
  <div class="book-cover">
    <div class="edge-band edge-band--left"></div>
    <div class="edge-band edge-band--right"></div>
    <div class="figure-art" role="img" aria-label="Two dark silhouettes of a woman, before and after weight loss, facing each other"></div>
    <h1 class="title">FOLDING<br>THE MAP</h1>
    <p class="subtitle">For Losing All The Weight You Want<br>&amp; Keeping It Off Forever<br>No Matter What You Have Tried in The Past</p>
    <div class="secrets-band">
      <div class="secrets-band__rule secrets-band__rule--top"></div>
      <div class="secrets-band__label">WEIGHT LOSS SECRETS</div>
      <div class="secrets-band__rule secrets-band__rule--bottom"></div>
    </div>
    <p class="author">COLIN MAYHEW</p>
  </div>
</div>
</body>
</html>
```